Cyber security firm needs to have a new look and modren website design

Vaultline Corp is already established and looking to improve the feel and UI of the site and cause potential clients to say "wow, let's contact them".
We provide cybersecurity assessment consulting services helping our clients to feel safer than they are now with a straightforward approach to data safety, as the current frameworks and regulations are NOT affective anymore.

the current site is: www.vaultline-example.biz

Please check the following sites:
norvekta-example.com
brimstalk-defense.example.com
https://www.quillmarsh-example.com

HomePage Design:
In general: we want to tell the viewer that it's a digital war out there, which is not a simple one. If not taking care of it will have causalities: https://www.quillmarsh-example.com/ see picture? See that and some what I'm afraid.... I need some assurance and safety...
1. Do not use the existing site content / design.
2. Do not use the 3 simple steps
3. Have slides top as it is now:
A Hacker Is Knocking, Are You READY? (and a matching picture)
4. Contact form on the right
5. 4 block services:
Web Application Security.
Internal / External Vulnerability Assessments.
Penetration Testing.
Malware Attack Simulation.
6. Recent News: 3 Blocks
7. Recent Posts: 3 Blocks
8. Under the contact form: Download out FREE Report Cybersecurity Assessment Framework
9. Top contact form search line.
10. Bottom page should show all links from top menu
11. This design should work on WordPress

Thanks.

Target Market(s)

Right now: Financials.
Looking to have to add more, will decide later.

Industry/Entity Type

Security

Coding

Coded - Design and coding required

Number of Pages Required

5+ page

Font styles to use
Other font styles liked:
• Caliberi

Requirements
Must have
• Our site is based on CMS: WordPress
• Should be progressive: to be showed on any device: PC, tablets and phones.
• Browsers: IE, Chrome and Firefox.
• Look serious, experts in their field and getting tasks done!
• Use the same fonts from:
• norvekta-example.com
• brimstalk-defense.example.com
• https://www.quillmarsh-example.com

```html
<!DOCTYPE html>
<html lang="en">
<head>
<meta charset="utf-8">
<title>Vaultline Corp — Safeguarding your data</title>
<link rel="stylesheet" href="https://fonts.googleapis.com/css2?family=Carlito:ital,wght@0,400;0,700;1,400;1,700&family=Open+Sans:ital,wght@0,600;0,700;1,700&display=swap">
<style>
:root{
  --navy:#06202f;
  --navy-2:#0b3550;
  --steel:#5f8aa0;
  --panel:#0f3c55;
  --ink:#0d1c24;
  --white:#ffffff;
  --title-blue:#9fd3f0;
  --link-blue:#2f8fd0;
  --card:#7fa3b6;
  --card-edge:#9cbccc;
  --button:#1d4a63;
  --input-text:#8a9aa3;
  --pdf-red:#c8201c;
}
*{box-sizing:border-box;margin:0;padding:0}
html,body{width:1200px;height:2429px;overflow:hidden}
body{position:relative;font-family:"Carlito",Calibri,sans-serif;color:var(--ink);
  background:linear-gradient(180deg,var(--steel) 0%,#6f97ab 25%,#5a8498 60%,#2f5366 85%,#08151d 100%)}
.abs{position:absolute}
/* header */
.site-header{left:0;top:0;width:1200px;height:117px;background:linear-gradient(180deg,#021019,var(--navy-2));z-index:2}
.nav a{position:absolute;top:46px;color:var(--white);font:italic 700 24px "Carlito",sans-serif;text-decoration:none}
.brand{left:434px;top:0;width:335px;height:146px;background:#03121c;z-index:3;text-align:center;padding-top:30px}
.brand-name{color:#1f86c8;font:700 52px/1 "Carlito",sans-serif;letter-spacing:1px}
.brand-tag{color:#5a9cc4;font:400 22px "Carlito",sans-serif;margin-top:4px}
.hero{left:0;top:117px;width:1200px;height:450px;background:radial-gradient(ellipse at 52% 40%,#8fd6e8 0%,#3e7f98 25%,#173e52 60%,#0a2433 100%)}
.hero h1{position:absolute;left:57px;top:95px;color:var(--white);font:italic 700 45px/56px "Carlito",sans-serif;text-shadow:2px 3px 4px #000}
.hero h1 span{display:block;padding-left:70px}
/* services */
.service h2{color:var(--title-blue);font:700 21px/28px "Open Sans",sans-serif;text-transform:uppercase;text-shadow:0 0 2px #0b3550,1px 1px 0 #0b3550}
.service p{color:var(--white);font-size:19.5px;line-height:25px;margin:10px 0 0 38px;width:680px}
.search{left:805px;top:605px;width:382px;height:46px;border-radius:23px;background:#aec6d2}
.form-panel{left:805px;top:669px;width:385px;height:521px;background:var(--panel);border-top:3px solid #0a2b3d}
.form-panel h3{position:absolute;left:22px;top:14px;color:#cfe4ef;font:italic 400 23px "Carlito",sans-serif}
.field{position:absolute;left:14px;width:360px;height:36px;background:var(--white);border-radius:5px;color:var(--input-text);font-size:19px;padding:7px 14px}
.btn{position:absolute;color:var(--white);font:700 19px "Carlito",sans-serif;text-align:center;border-radius:3px;background:linear-gradient(180deg,#4b7a93,var(--button));box-shadow:0 2px 3px rgba(0,0,0,.5)}
.submit{left:194px;top:455px;width:178px;height:40px;line-height:40px;background:#8fc3e0;color:#0b3550;font-size:18px;text-align:center;border-radius:6px}
.download{left:837px;top:1201px;width:326px;height:57px;background:linear-gradient(180deg,#fff,#cfd6da);border-radius:2px}
.download .pdf{position:absolute;left:0;top:0;width:52px;height:57px;background:var(--pdf-red)}
.download b{position:absolute;left:62px;top:4px;color:var(--pdf-red);font:700 26px "Carlito",sans-serif}
.download small{position:absolute;left:62px;top:34px;color:#777;font:700 14px "Carlito",sans-serif;white-space:nowrap}
.section-title{left:0;width:1200px;text-align:center;color:#dfe9ee;font:700 44px "Open Sans",sans-serif;text-shadow:1px 2px 3px #0b2230}
/* news */
.news{width:350px;height:470px;background:linear-gradient(180deg,#6e98ad,#5a8397)}
.news .thumb{position:absolute;left:15px;top:10px;width:320px;height:200px;background:linear-gradient(180deg,#f2f4f6,#d8dee2);border:1px solid #c7d3d9}
.news h4{position:absolute;left:5px;top:226px;width:340px;text-align:center;color:var(--white);font:italic 700 20px/28px "Open Sans",sans-serif}
.news .meta{position:absolute;left:10px;width:330px;text-align:center;color:var(--link-blue);font:700 13px "Carlito",sans-serif;text-transform:uppercase}
.news .body{position:absolute;left:14px;width:326px;color:var(--white);font-size:14.5px;line-height:17.5px}
.news .body span{display:block;text-indent:20px}
/* posts */
.post{width:342px;height:260px;border-radius:12px;background:var(--card);border:1px solid var(--card-edge);box-shadow:0 2px 4px rgba(0,0,0,.3)}
.post h5{position:absolute;left:26px;top:12px;color:var(--white);font:700 20px "Open Sans",sans-serif}
.post p{position:absolute;left:26px;top:48px;width:300px;color:var(--white);font-size:14.5px;line-height:18px;text-indent:20px}
.post a{position:absolute;right:18px;bottom:10px;color:#13415c;font-size:17px;line-height:22px;text-decoration:underline}
/* footer */
.footer{left:0;top:2372px;width:1200px;height:57px}
.footer .copy{position:absolute;left:14px;top:14px;color:#8fa2ad;font-size:17px}
.footer a{position:absolute;top:14px;color:var(--white);font-size:17px;text-decoration:none}
</style>
</head>
<body>
<header class="abs site-header">
  <nav class="nav">
    <a style="left:35px">HOME</a><a style="left:160px">WHY US?</a><a style="left:322px">SERVICES</a>
    <a style="left:792px">ABOUT US</a><a style="left:952px">MEDIA</a><a style="left:1080px">CONTACT</a>
  </nav>
</header>
<div class="abs brand"><div class="brand-name">VAULTLINE</div><div class="brand-tag">safeguarding your data</div></div>

<section class="abs hero" role="img" aria-label="Futuristic glowing digital corridor with a bright light beam">
  <h1>A Hacker is Knocking<span>Are You Ready?</span></h1>
</section>

<div class="abs service" style="left:57px;top:615px">
  <h2>Web Application Security</h2>
  <p>There is no doubt that every business is integrating web applications or already done so to allow employees and customers to interact on daily basis. This can be an employee who is checking his or her emails or a customer placing an order thru a shopping cart application.</p>
</div>
<div class="abs service" style="left:57px;top:760px">
  <h2>Internal / External Vulnerability Assessments</h2>
  <p>Based on our experience from past customers it is recommended to perform a full security analysis that will include Internal and external perimeters. The full analysis will provide a complete and current security posture of the organization.</p>
</div>
<div class="abs service" style="left:64px;top:903px">
  <h2>Penetration Testing</h2>
  <p style="margin-left:31px">Penetration testing AKA pen-testing is a process where a tester looks for exploitable vulnerabilities from within an IT infrastructure that may allow the tester to subvert, modify and extract information.</p>
</div>
<div class="abs service" style="left:64px;top:1030px">
  <h2>Malware Attack Simulation</h2>
  <p style="margin-left:31px">Sem Nulla consequat massa quis enim. Donec pede justo, fringilla vel, aliquet nec, vulputate eget, arcu. In enim justo, rhoncus ut, imperdiet a, venenatis vitae, justo. Nullam dictum felis eu pede mollis pretium.</p>
</div>
<div class="btn" style="left:625px;top:1200px;width:168px;height:39px;line-height:39px;font-weight:400">Learn More</div>

<div class="abs search">
  <svg class="abs" style="left:6px;top:4px" width="38" height="38" viewBox="0 0 38 38" fill="none" stroke="#1b2b33" stroke-width="2.5"><circle cx="16" cy="16" r="11"/><line x1="24" y1="24" x2="34" y2="34"/></svg>
</div>
<form class="abs form-panel">
  <h3>Submit an inquiry</h3>
  <div class="field" style="top:55px">First Name</div>
  <div class="field" style="top:110px">Last Name</div>
  <div class="field" style="top:163px">Email Address</div>
  <div class="field" style="top:218px">Company Name</div>
  <div class="field" style="top:270px;height:157px">Your inquiry here...</div>
  <div class="submit abs">SUBMIT INQUIRY</div>
</form>
<div class="abs download">
  <div class="pdf"><svg width="52" height="57" viewBox="0 0 52 57"><text x="26" y="48" fill="#fff" font-family="Carlito,sans-serif" font-size="13" text-anchor="middle">PDF</text></svg></div>
  <b>FREE DOWNLOAD</b><small>Report Cybersecurity Assessment Framework</small>
</div>

<h2 class="abs section-title" style="top:1305px">RECENT NEWS</h2>
<article class="abs news" style="left:23px;top:1373px">
  <div class="thumb" role="img" aria-label="Screenshot of a news article page about cybersecurity in the C-suite"></div>
  <h4>Cybersecurity in the C-Suite: A Matter of “Need to Know”</h4>
  <div class="meta" style="top:288px">March 11, 2015, by Dana Merrow</div>
  <div class="body" style="top:322px"><span>Cybersecurity has been described as everything from a top-down corporate mission to a shopping list for software packages that monitor networks and systems for suspicious activity. Given the breadth and complexity of even identifying the risks, it’s no wonder that all sorts of management are discovering they’re now riding the cybersecurity bus.</span></div>
</article>
<article class="abs news" style="left:424px;top:1373px">
  <div class="thumb" role="img" aria-label="Screenshot of a news article page about fund managers hiring cybersecurity officers"></div>
  <h4>Fund Managers: On the Hunt for New CyberSecurity Officer</h4>
  <div class="meta" style="top:288px">September 22, 2014, by Dana Merrow</div>
  <div class="body" style="top:322px"><span>With the Securities and Exchange Commission now requiring registered investment advisers to prove they are doing their best to reduce the risk of data and other security breaches, hedge fund managers are quickly waking up to the need to assign a dedicated chief security information officer (CISO) to the task. Although the SEC’s guidelines...</span></div>
</article>
<article class="abs news" style="left:826px;top:1373px">
  <div class="abs" style="left:20px;top:18px;width:305px;height:55px;background:#5c8a2e;color:#fff;font:700 24px/55px 'Carlito',sans-serif;text-align:center">Ledger Street Tech</div>
  <h4 style="top:98px;font-size:19px">Hedge Funds Raise the Urgency Level on Cyber Security</h4>
  <div class="meta" style="top:160px;font-weight:400;text-transform:none">August 28, 2014, By Lena Voskuil</div>
  <div class="body" style="top:186px;font-size:14px;line-height:17px"><span>Hedge funds are bracing for SEC exams on cyber security preparedness in 2014, but do they need a chief information security officer?</span><span>Hedge funds are paying more attention to cyber security as a result of recent guidance from the Securities and Exchange Commission.</span><span>An April risk alert has raised the urgency level for alternative funds registered with the US regulatory body to assess information security and test for any vulnerabilities. The SEC’s Office of Compliance Inspections and Examinations (OCIE) notified hedge funds and more than 50 registered broker dealers and investment advisers that the agency’s 2014 examinations would focus on cyber security preparedness. The OCIE has given the funds a questionnaire to fill out.</span></div>
</article>
<div class="btn" style="left:193px;top:1851px;width:166px;height:38px;line-height:38px">Read More</div>
<div class="btn" style="left:595px;top:1851px;width:166px;height:38px;line-height:38px">Read More</div>
<div class="btn" style="left:1003px;top:1851px;width:166px;height:38px;line-height:38px">Read More</div>

<h2 class="abs section-title" style="top:1918px">RECENT POSTS</h2>
<article class="abs post" style="left:24px;top:1993px"><h5>Lorem ipsum dolor sit amet</h5><p>consectetuer adipiscing elit. Aenean commodo ligula eget dolor. Aenean massa. Cum sociis natoque penatibus et magnis dis parturient montes, nascetur ridiculus mus. Donec quam felis, ultricies nec, pellentesque eu, pretium quis sem. Nulla consequat massa quis enim. Donec pede justo, fringilla vel, aliquet nec, vulputate eget, arcu. In enim justo, rhoncus ut, imperdiet a, venenatis vitae, justo. Nullam dictum felis eu pede mollis pretium...</p><a>Continue reading</a></article>
<article class="abs post" style="left:429px;top:1993px"><h5>Lorem ipsum dolor sit amet</h5><p>consectetuer adipiscing elit. Aenean commodo ligula eget dolor. Aenean massa. Cum sociis natoque penatibus et magnis dis parturient montes, nascetur ridiculus mus. Donec quam felis, ultricies nec, pellentesque eu, pretium quis sem. Nulla consequat massa quis enim. Donec pede justo, fringilla vel, aliquet nec, vulputate eget, arcu. In enim justo, rhoncus ut, imperdiet a, venenatis vitae, justo. Nullam dictum felis eu pede mollis pretium...</p><a>Continue reading</a></article>
<article class="abs post" style="left:834px;top:1993px"><h5>Lorem ipsum dolor sit amet</h5><p>consectetuer adipiscing elit. Aenean commodo ligula eget dolor. Aenean massa. Cum sociis natoque penatibus et magnis dis parturient montes, nascetur ridiculus mus. Donec quam felis, ultricies nec, pellentesque eu, pretium quis sem. Nulla consequat massa quis enim. Donec pede justo, fringilla vel, aliquet nec, vulputate eget, arcu. In enim justo, rhoncus ut, imperdiet a, venenatis vitae, justo. Nullam dictum felis eu pede mollis pretium...</p><a>Continue reading</a></article>

<footer class="abs footer">
  <span class="copy">© All rights reserved Vaultline Corp 2003-2015</span>
  <a style="left:557px">HOME</a><a style="left:649px">WHY US?</a><a style="left:758px">SERVICES</a>
  <a style="left:866px">ABOUT US</a><a style="left:991px;color:#b8c6ce">MEDIA</a><a style="left:1081px">CONTACT</a>
</footer>
</body>
</html>
```